Product presentation and placement brochure

I have cardiovascular exercise equipment (treadmill, bikes, eliptical trainers, etc.) that have a coin timers attached that allow use of this exercise equipment using coins. I want to market to apartment buildings, swimming pools, training gyms, etc. We want them to partner with us by allowing us to place our equipment in their locations. Their residents would get new equipment to use, they use a coin to get so much time. The apartment building doesn't pay anything precharge us workspace, but they will get a 10 - 20% of all the revenue that flows through the machines in their building.This brochure needs to clearly display our equipment, how the residents can use it, the ease of the relationship between us and the apartment building, and how they will make money with no investment and no commitment.I would, like the brochure to look artistic, not so mechanical.

Target Market(s)

Large apartment buildings, Public swimming pools, training studios, gyms, etc.

Font styles to use
Serif

Colors

Designer to choose colors to be used in the design.

Requirements
Must have
• The basic wording for the brochure. Must have English and Chinese.
• Vero Pulse Machine Brochure
• 維諾脈動健身器材指南
• We will pay YOU to let us provide YOU with commercial cardiovascular equipment.
• 我們付你錢來讓我們提供你有氧器材
• We supply cardio equipment to your residents at no cost to you. In fact, we will pay you! Please take a moment to look at our brochure and see how we can work with you and your homeowners association to bring the latest in fitness technology to your building, and we’ll pay you for it.
• 在不花費你任何金錢的情況下, 我們提供有氧器材給你的住戶。甚至我們付你錢!請看我們的手冊來了解我們如何能和你跟社區管理委員會合作, 把最新的健身器材介紹到你的大樓, 並且帶給你收益。
• Our machines are all equipped with patented coin operated technology. If your residents would like to have the luxury of quality exercise, they may insert dollars for minutes.
• 我們的器材皆具備專利通過投幣式設計。如果你的住戶想要享有高品質運動, 他們可以投幣來取得運動時間。
• By the 10th of every month, we will pay 15% of all revenue collected for the previous month, minus taxes, to you or your homeowners association, whichever you choose.
• 每個月10號, 我們將付你或社區管理委員會前一個月百分之十五不含稅的收入。
• Why it is so easy:
• 1. We provide the equipment at no cost to you.
• 2. We pay for shipping and installation.
• 3. Month-to-month agreement, no commitment from you.
• 4. Removal with 30 days notice, no questions asked.
• 5. We conduct all repairs and regular maintenance.
• 6. We will pay you from the revenue collected!
• 為什麼超簡單:
• 1. 不花你一毛錢, 器材我們提供。
• 2. 運送費跟安裝費, 全數我們支付。
• 3. 以一個月為一期, 不用長期保證。
• 4. 30天移出通知, 不需任何理由。
• 5. 所有器材維修, 我們負責。
• 6. 器材收益,我們分享!
• As easy as 1, 2, 3!
• 簡單有如1, 2, 3!
• STEP 1
• We have several different machine types that will motivate your residents to exercise:
• 1. Treadmill (photo and stats.)
• 2. Recumbent Bike (photo and stats.)
• 3. Regular Seated Bike (photo and stats.)
• 4. Elliptical trainer (photo and stats.)
• Replace old equipment, broken equipment, or just place new equipment next to your old equipment.
• 第一步
• 我們有多種有氧器材可讓住戶更有動力運動:
• 1. 跑步機
• 2. 臥式腳踏車
• 3. 直立式腳踏車
• 4. 橢圓機
• 替換原有老舊的運動器材, 或是直接放一台新的器材在原有器材的旁邊。
• After meeting with you and determining you and your residents needs, we will decide how many and of what types of equipment you would like in your exercise room.
• 在和你會面並且評估你和住戶的需求後, 我們會決定你想要的器材種類和數量。
• STEP 2
• We will deliver and install the equipment, in a suitable location that you choose. All at no cost to you!
• 第二步
• 我們將器材運送到你選擇的合適場所並安裝。不需任何費用!
• Step 3
• 第三步
• Make your residents healthy and happy by letting them use any of the equipment, for as long as they like, at their leisure.
• 住戶可盡情使用任何器材, 讓住戶健康又開心。
• Photo Steps on how to use equipment
• 0. 2. 3.
• We would be happy to answer any of your questions and give you a free consultation on how you can utilize this service to bring affordable fitness to your residents, while creating a revenue stream for you or your homeowners association.
• 我們很樂意回答任何問題並免費提供諮詢:如何有效利用此服務以帶給住戶能負擔的健身運動, 且同時創造收益給你或社區管理委員會。
• For more Information, please:
• visit our website at:
• call:
• Email:
• 更多資訊請:
• 拜訪我們的網站:
• 電話聯絡:
• 傳送電子郵件:
• Quentin Hale
• Marisol Tevet
• Vero Pulse Fitness
• Manager of Marketing and English Translation
• Ph: +17605550187
• LINE ID: driftingotter
• Email: drifting-otter@mailvoro.com
Nice to have
• I would like it to be have a high tech artsy feel. I don't want the haredline industrial.

```html
<!DOCTYPE html>
<html lang="en">
<head>
<meta charset="utf-8">
<title>Vero Pulse Machine Brochure</title>
<link rel="stylesheet" href="https://fonts.googleapis.com/css2?family=Oswald:wght@500;700&family=Open+Sans:wght@400;600;700&family=Noto+Sans+TC:wght@400;700&display=swap">
<style>
  :root{
    --yellow:#f3c623;
    --yellow-deep:#e2ad10;
    --ink:#161616;
    --charcoal:#2a2a2a;
    --paper:#ffffff;
    --text:#3b3b3b;
    --muted:#6a6a6a;
    --backdrop:#e7e8ea;
  }
  *{box-sizing:border-box;margin:0;padding:0}
  html,body{width:1200px;height:2446px;overflow:hidden}
  body{background:var(--backdrop);font-family:"Open Sans","Noto Sans TC",sans-serif;color:var(--text)}
  .canvas{position:relative;width:1200px;height:2446px}

  .page{position:absolute;width:520px;height:735px;background:var(--paper);overflow:hidden;box-shadow:0 14px 30px rgba(0,0,0,.18)}
  .spread{position:absolute;width:1040px;height:735px;box-shadow:0 16px 34px rgba(0,0,0,.2)}
  .spread .page{box-shadow:none;top:0}
  .spread .page--left{left:0}
  .spread .page--right{left:520px}
  .spread::after{content:"";position:absolute;left:508px;top:0;width:24px;height:735px;background:linear-gradient(90deg,rgba(0,0,0,0),rgba(0,0,0,.12) 50%,rgba(0,0,0,0));pointer-events:none}

  .cover{left:340px;top:40px}
  .spread--outer{left:80px;top:850px}
  .spread--inner{left:80px;top:1670px}

  .art{position:absolute;left:0;top:0;width:520px;height:735px}

  .headline{position:absolute;left:30px;top:58px;width:280px;font-family:"Oswald",sans-serif;font-weight:700;font-size:21px;line-height:1.15;text-transform:uppercase;color:var(--ink)}
  .headline em{font-style:normal;color:var(--paper)}
  .headline-zh{position:absolute;left:30px;top:150px;width:300px;font-family:"Noto Sans TC",sans-serif;font-weight:700;font-size:15px;color:var(--ink)}

  .brand{position:absolute;display:flex;align-items:center;gap:10px}
  .brand__dot{width:64px;height:64px;border-radius:50%;background:var(--ink);flex:none}
  .brand__name{font-family:"Oswald",sans-serif;font-weight:700;font-size:15px;line-height:1.1;text-transform:uppercase;color:var(--ink);width:90px}
  .cover .brand,.page--right .brand--cover{left:345px;top:48px}

  .web-pill{position:absolute;display:flex;align-items:center;gap:7px;height:24px;padding:0 16px 0 6px;border-radius:12px;background:var(--yellow);border:2px solid var(--ink);font-size:11px;font-weight:700;color:var(--ink)}
  .web-pill__dot{width:13px;height:13px;border-radius:50%;background:var(--ink)}

  .contact-copy{position:absolute;left:26px;top:20px;width:468px;font-size:7.3px;line-height:1.45;color:var(--ink)}
  .contact-copy p+p{margin-top:3px}
  .contact-cols{position:absolute;left:26px;top:80px;width:468px;display:flex;gap:26px;font-size:7.3px;line-height:1.5;color:var(--ink)}
  .contact-cols > div{flex:1}
  .contact-cols strong{font-weight:700}
  .contact-line{position:absolute;left:26px;top:170px;display:flex;align-items:center;gap:6px;font-size:7.5px;font-weight:700;color:var(--ink)}
  .contact-line span.icon{width:12px;height:12px;border-radius:50%;background:var(--ink)}

  .intro{position:absolute;left:26px;top:238px;width:468px;font-size:7.4px;line-height:1.5;color:var(--text)}
  .intro p+p{margin-top:5px}
  .ease{position:absolute;top:440px;width:222px}
  .ease--en{left:26px}
  .ease--zh{left:272px}
  .ease__label{display:inline-block;background:var(--yellow);color:var(--ink);font-weight:700;font-size:10px;padding:4px 10px;margin-bottom:8px}
  .ease__list{list-style:none;font-size:7.6px;line-height:1.4}
  .ease__list li{position:relative;padding-left:15px;margin-bottom:6px}
  .ease__list li::before{content:"";position:absolute;left:0;top:1px;width:9px;height:9px;background:var(--yellow);border-radius:50%}
  .ease__list li::after{content:"";position:absolute;left:2.5px;top:3px;width:3px;height:4px;border:solid var(--ink);border-width:0 1.3px 1.3px 0;transform:rotate(45deg)}

  .brand--inner{left:22px;top:22px}
  .brand--inner .brand__dot{width:54px;height:54px}
  .brand--inner .brand__name{font-size:13px;width:80px}

  .steps-title{position:absolute;left:26px;top:186px;font-family:"Oswald",sans-serif;font-weight:500;font-size:15px;color:var(--ink)}
  .step{position:absolute;left:26px;width:468px;display:flex;gap:12px}
  .step__photo{flex:none;width:104px}
  .step__body{flex:1}
  .step__bar{display:flex;align-items:center;justify-content:space-between;background:var(--ink);height:20px;padding-right:10px;margin-bottom:6px}
  .step__tag{background:var(--yellow);color:var(--ink);font-family:"Oswald",sans-serif;font-weight:700;font-size:11px;height:20px;line-height:20px;padding:0 10px}
  .step__tag-zh{color:var(--yellow);font-size:9px;font-weight:700}
  .step__text{font-size:7.2px;line-height:1.45;color:var(--text)}
  .step__text p+p{margin-top:3px}
  .step--one{top:218px}
  .step--two{top:450px}
  .step--three{top:560px}
</style>
</head>
<body>
<div class="canvas">

  <svg width="0" height="0" style="position:absolute" aria-hidden="true">
    <defs>
      <linearGradient id="gymFloor" x1="0" y1="0" x2="0" y2="1">
        <stop offset="0" stop-color="#2b2f3a"/>
        <stop offset=".3" stop-color="#5d6577"/>
        <stop offset=".55" stop-color="#9aa2b4"/>
        <stop offset=".8" stop-color="#c9cdd8"/>
        <stop offset="1" stop-color="#8c92a2"/>
      </linearGradient>
      <radialGradient id="gymGlow" cx=".75" cy=".35" r=".5">
        <stop offset="0" stop-color="#e8e4d2" stop-opacity=".75"/>
        <stop offset="1" stop-color="#e8e4d2" stop-opacity="0"/>
      </radialGradient>
      <linearGradient id="trainerTone" x1="0" y1="0" x2="1" y2="1">
        <stop offset="0" stop-color="#1f2228"/>
        <stop offset=".45" stop-color="#555a66"/>
        <stop offset="1" stop-color="#2a2c32"/>
      </linearGradient>
      <radialGradient id="warmFlare" cx=".8" cy=".15" r=".55">
        <stop offset="0" stop-color="#ff8a3d" stop-opacity=".9"/>
        <stop offset=".5" stop-color="#c25a2a" stop-opacity=".45"/>
        <stop offset="1" stop-color="#c25a2a" stop-opacity="0"/>
      </radialGradient>
      <linearGradient id="roomTone" x1="0" y1="0" x2="1" y2="0">
        <stop offset="0" stop-color="#8a3a22"/>
        <stop offset=".35" stop-color="#b4552f"/>
        <stop offset=".6" stop-color="#8f939c"/>
        <stop offset="1" stop-color="#dfe0e3"/>
      </linearGradient>
      <linearGradient id="roomFloor" x1="0" y1="0" x2="0" y2="1">
        <stop offset="0" stop-color="#000" stop-opacity="0"/>
        <stop offset="1" stop-color="#ececec" stop-opacity=".8"/>
      </linearGradient>
      <linearGradient id="runnerTone" x1="0" y1="0" x2="1" y2="0">
        <stop offset="0" stop-color="#e9dccd"/>
        <stop offset=".45" stop-color="#b89a84"/>
        <stop offset=".75" stop-color="#5e4a40"/>
        <stop offset="1" stop-color="#2f2826"/>
      </linearGradient>
      <linearGradient id="stepMachines" x1="0" y1="0" x2="0" y2="1">
        <stop offset="0" stop-color="#7c818c"/>
        <stop offset=".48" stop-color="#b9bcc3"/>
        <stop offset=".52" stop-color="#e3bd3a"/>
        <stop offset="1" stop-color="#8c7a3a"/>
      </linearGradient>
      <linearGradient id="stepDelivery" x1="0" y1="0" x2="1" y2="1">
        <stop offset="0" stop-color="#d8d2c6"/>
        <stop offset=".6" stop-color="#8e8478"/>
        <stop offset="1" stop-color="#4a433c"/>
      </linearGradient>
      <linearGradient id="stepUse" x1="0" y1="0" x2="1" y2="1">
        <stop offset="0" stop-color="#cfd2d8"/>
        <stop offset=".5" stop-color="#6f747e"/>
        <stop offset="1" stop-color="#2c2f36"/>
      </linearGradient>
    </defs>
  </svg>

  <!-- Front cover -->
  <div class="page cover">
    <svg class="art" viewBox="0 0 520 735" aria-hidden="true">
      <rect width="520" height="320" fill="var(--yellow)"/>
      <path d="M0,0 L520,0 L520,120 Q300,40 0,150 Z" fill="var(--yellow-deep)" opacity=".35"/>
      <path d="M0,250 Q250,175 520,215 L520,300 Q260,250 0,330 Z" fill="var(--ink)"/>
    </svg>
    <svg class="art" viewBox="0 0 520 735" role="img" aria-label="Photo of a gym floor lined with treadmills and cardio machines">
      <path d="M0,318 Q260,240 520,290 L520,735 L0,735 Z" fill="url(#gymFloor)"/>
      <path d="M0,318 Q260,240 520,290 L520,735 L0,735 Z" fill="url(#gymGlow)"/>
    </svg>
    <div class="headline"><em>We will pay you</em> to let us provide you with commercial cardiovascular equipment.</div>
    <div class="headline-zh" lang="zh-Hant">我們付你錢來讓我們提供你有氧器材</div>
    <div class="brand"><span class="brand__dot"></span><span class="brand__name">Vero Pulse Fitness</span></div>
    <div class="web-pill" style="left:210px;bottom:26px"><span class="web-pill__dot"></span>www.veropulsefitness.com</div>
  </div>

  <!-- Back and front covers -->
  <div class="spread spread--outer">
    <div class="page page--left">
      <svg class="art" viewBox="0 0 520 735" aria-hidden="true">
        <rect width="520" height="330" fill="var(--yellow)"/>
        <g transform="translate(520,0) scale(-1,1)">
          <path d="M0,250 Q250,175 520,215 L520,300 Q260,250 0,330 Z" fill="var(--ink)"/>
        </g>
      </svg>
      <svg class="art" viewBox="0 0 520 735" role="img" aria-label="Photo of a woman training on an elliptical machine in a gym">
        <g transform="translate(520,0) scale(-1,1)">
          <path d="M0,318 Q260,240 520,290 L520,735 L0,735 Z" fill="url(#trainerTone)"/>
          <path d="M0,318 Q260,240 520,290 L520,735 L0,735 Z" fill="url(#warmFlare)" transform="translate(520,0) scale(-1,1)"/>
        </g>
      </svg>
      <div class="contact-copy">
        <p>We would be happy to answer any of your questions and give you a free consultation on how you can utilize this service to bring affordable fitness to your residents, while creating a revenue stream for you or your homeowners association.</p>
        <p lang="zh-Hant">我們很樂意回答任何問題並免費提供諮詢:如何有效利用此服務以帶給住戶能負擔的健身運動, 且同時創造收益給你或社區管理委員會。</p>
      </div>
      <div class="contact-cols">
        <div>
          <strong>For more Information, please:</strong><br>
          visit our website at: www.veropulsefitness.com<br>
          call: +17605550187<br>
          Email: drifting-otter@mailvoro.com<br>
          <strong>Quentin Hale</strong><br>Vero Pulse Fitness
        </div>
        <div lang="zh-Hant">
          <strong>更多資訊請:</strong><br>
          拜訪我們的網站: www.veropulsefitness.com<br>
          電話聯絡: +17605550187<br>
          傳送電子郵件: drifting-otter@mailvoro.com<br>
          <strong lang="en">Marisol Tevet</strong><br><span lang="en">Manager of Marketing and English Translation</span>
        </div>
      </div>
      <div class="contact-line"><span class="icon"></span>Ph: +17605550187 &nbsp; LINE ID: driftingotter</div>
      <div class="web-pill" style="left:34px;bottom:26px"><span class="web-pill__dot"></span>www.veropulsefitness.com</div>
    </div>

    <div class="page page--right">
      <svg class="art" viewBox="0 0 520 735" aria-hidden="true">
        <rect width="520" height="320" fill="var(--yellow)"/>
        <path d="M0,0 L520,0 L520,120 Q300,40 0,150 Z" fill="var(--yellow-deep)" opacity=".35"/>
        <path d="M0,250 Q250,175 520,215 L520,300 Q260,250 0,330 Z" fill="var(--ink)"/>
      </svg>
      <svg class="art" viewBox="0 0 520 735" role="img" aria-label="Photo of a gym floor lined with treadmills and cardio machines">
        <path d="M0,318 Q260,240 520,290 L520,735 L0,735 Z" fill="url(#gymFloor)"/>
        <path d="M0,318 Q260,240 520,290 L520,735 L0,735 Z" fill="url(#gymGlow)"/>
      </svg>
      <div class="headline"><em>We will pay you</em> to let us provide you with commercial cardiovascular equipment.</div>
      <div class="headline-zh" lang="zh-Hant">我們付你錢來讓我們提供你有氧器材</div>
      <div class="brand brand--cover"><span class="brand__dot"></span><span class="brand__name">Vero Pulse Fitness</span></div>
      <div class="web-pill" style="left:210px;bottom:26px"><span class="web-pill__dot"></span>www.veropulsefitness.com</div>
    </div>
  </div>

  <!-- Inside spread -->
  <div class="spread spread--inner">
    <div class="page page--left">
      <svg class="art" viewBox="0 0 520 735" role="img" aria-label="Photo of exercise bikes and a treadmill in a bright fitness room">
        <path d="M0,0 L520,0 L520,170 Q260,230 0,205 Z" fill="url(#roomTone)"/>
        <path d="M0,0 L520,0 L520,170 Q260,230 0,205 Z" fill="url(#roomFloor)"/>
      </svg>
      <svg class="art" viewBox="0 0 520 735" aria-hidden="true">
        <path d="M0,205 Q260,230 520,170 L520,182 Q260,244 0,218 Z" fill="var(--yellow)"/>
      </svg>
      <div class="intro">
        <p>We supply cardio equipment to your residents at no cost to you. In fact, we will pay you! Please take a moment to look at our brochure and see how we can work with you and your homeowners association to bring the latest in fitness technology to your building, and we’ll pay you for it.</p>
        <p lang="zh-Hant">在不花費你任何金錢的情況下, 我們提供有氧器材給你的住戶。甚至我們付你錢!請看我們的手冊來了解我們如何能和你跟社區管理委員會合作, 把最新的健身器材介紹到你的大樓, 並且帶給你收益。</p>
        <p>Our machines are all equipped with patented coin operated technology. If your residents would like to have the luxury of quality exercise, they may insert dollars for minutes.</p>
        <p lang="zh-Hant">我們的器材皆具備專利通過投幣式設計。如果你的住戶想要享有高品質運動, 他們可以投幣來取得運動時間。</p>
        <p>By the 10th of every month, we will pay 15% of all revenue collected for the previous month, minus taxes, to you or your homeowners association, whichever you choose.</p>
        <p lang="zh-Hant">每個月10號, 我們將付你或社區管理委員會前一個月百分之十五不含稅的收入。</p>
      </div>
      <div class="ease ease--en">
        <span class="ease__label">Why it is so easy:</span>
        <ul class="ease__list">
          <li>We provide the equipment at no cost to you.</li>
          <li>We pay for shipping and installation.</li>
          <li>Month-to-month agreement, no commitment from you.</li>
          <li>Removal with 30 days notice, no questions asked.</li>
          <li>We conduct all repairs and regular maintenance.</li>
          <li>We will pay you from the revenue collected!</li>
        </ul>
      </div>
      <div class="ease ease--zh" lang="zh-Hant">
        <span class="ease__label">為什麼超簡單:</span>
        <ul class="ease__list">
          <li>不花你一毛錢, 器材我們提供。</li>
          <li>運送費跟安裝費, 全數我們支付。</li>
          <li>以一個月為一期, 不用長期保證。</li>
          <li>30天移出通知, 不需任何理由。</li>
          <li>所有器材維修, 我們負責。</li>
          <li>器材收益,我們分享!</li>
        </ul>
      </div>
    </div>

    <div class="page page--right">
      <svg class="art" viewBox="0 0 520 735" role="img" aria-label="Photo of women running on treadmills in a gym">
        <path d="M190,0 L520,0 L520,140 Q360,175 190,150 Z" fill="url(#runnerTone)"/>
      </svg>
      <svg class="art" viewBox="0 0 520 735" aria-hidden="true">
        <path d="M0,160 Q260,190 520,140 L520,152 Q260,204 0,172 Z" fill="var(--yellow)"/>
      </svg>
      <div class="brand brand--inner"><span class="brand__dot"></span><span class="brand__name">Vero Pulse Fitness</span></div>
      <div class="steps-title">As easy as 1, 2, 3! <span lang="zh-Hant">簡單有如1, 2, 3!</span></div>

      <div class="step step--one">
        <svg class="step__photo" height="210" viewBox="0 0 104 210" role="img" aria-label="Photos of the treadmill, recumbent bike, seated bike and elliptical trainer"><rect width="104" height="210" fill="url(#stepMachines)"/></svg>
        <div class="step__body">
          <div class="step__bar"><span class="step__tag">STEP 1</span><span class="step__tag-zh" lang="zh-Hant">第一步</span></div>
          <div class="step__text">
            <p>We have several different machine types that will motivate your residents to exercise: 1. Treadmill &nbsp;2. Recumbent Bike &nbsp;3. Regular Seated Bike &nbsp;4. Elliptical trainer</p>
            <p lang="zh-Hant">我們有多種有氧器材可讓住戶更有動力運動: 1. 跑步機 2. 臥式腳踏車 3. 直立式腳踏車 4. 橢圓機</p>
            <p>Replace old equipment, broken equipment, or just place new equipment next to your old equipment.</p>
            <p lang="zh-Hant">替換原有老舊的運動器材, 或是直接放一台新的器材在原有器材的旁邊。</p>
            <p>After meeting with you and determining you and your residents needs, we will decide how many and of what types of equipment you would like in your exercise room.</p>
            <p lang="zh-Hant">在和你會面並且評估你和住戶的需求後, 我們會決定你想要的器材種類和數量。</p>
          </div>
        </div>
      </div>

      <div class="step step--two">
        <svg class="step__photo" height="96" viewBox="0 0 104 96" role="img" aria-label="Photo of equipment being delivered and installed"><rect width="104" height="96" fill="url(#stepDelivery)"/></svg>
        <div class="step__body">
          <div class="step__bar"><span class="step__tag">STEP 2</span><span class="step__tag-zh" lang="zh-Hant">第二步</span></div>
          <div class="step__text">
            <p>We will deliver and install the equipment, in a suitable location that you choose. All at no cost to you!</p>
            <p lang="zh-Hant">我們將器材運送到你選擇的合適場所並安裝。不需任何費用!</p>
          </div>
        </div>
      </div>

      <div class="step step--three">
        <svg class="step__photo" height="150" viewBox="0 0 104 150" role="img" aria-label="Photo steps showing how residents use the coin operated machines"><rect width="104" height="150" fill="url(#stepUse)"/></svg>
        <div class="step__body">
          <div class="step__bar"><span class="step__tag">STEP 3</span><span class="step__tag-zh" lang="zh-Hant">第三步</span></div>
          <div class="step__text">
            <p>Make your residents healthy and happy by letting them use any of the equipment, for as long as they like, at their leisure.</p>
            <p lang="zh-Hant">住戶可盡情使用任何器材, 讓住戶健康又開心。</p>
          </div>
        </div>
      </div>
    </div>
  </div>

</div>
</body>
</html>
```